Create a MAIN PAGE that is so enticing they won't say no. -Velm Kor website

High traffic site but we are not closing the deal as much as we should. Our retention rate is 90%. We believe that our site is not properly conveying to our clients the wonderous, exotic and unique experiences we provide them. Our site must give the same impression we give in person. We are seeking a designer to revise our main page & booking pages as these are our calling card pages.
Our industry is selling fantasy and escapism. We want our main page to convey two high class, discreet, sexy dominatrix's.
We want our booking page to be user friendly.
www.quorvelstudio.example

Target Market(s)

Adult Men ages 45-65

Industry/Entity Type

Sex

Coding

Coded - Design and coding required

Number of Pages Required

2 page

Font styles to use
Serif

Colors
EB3D1F
EC4F4E
F09395
F8D3D4
FCEDEE

Requirements
Must have
• Black & Red color theme, animation, clean, classy, sexy
Nice to have
• Smoke effect on the main page
Should not have
• Should not look basic

```html
<!DOCTYPE html>
<html lang="en">
<head>
<meta charset="utf-8">
<title>Velm Kor Studio — Tag Team Duo</title>
<link rel="stylesheet" href="https://fonts.googleapis.com/css2?family=Anton&family=Inter:wght@400&display=swap">
<style>
  :root {
    --ink: #000000;
    --scarlet: #f40000;
    --paper: #ffffff;
    --smoke: rgba(190, 190, 190, 0.35);
    --photo-dark: #1a1414;
    --photo-mid: #5a4a44;
    --photo-light: #cbb9a8;
  }
  * { box-sizing: border-box; margin: 0; padding: 0; }
  html, body { width: 1200px; height: 800px; overflow: hidden; background: var(--ink); }
  .hero {
    position: relative;
    width: 1200px;
    height: 800px;
    overflow: hidden;
    background: linear-gradient(90deg, var(--ink) 0 49%, var(--scarlet) 49% 100%);
    font-family: "Inter", sans-serif;
    color: var(--paper);
  }
  .site-header {
    position: absolute;
    top: 82px;
    left: 0;
    width: 100%;
    height: 40px;
  }
  .menu-toggle {
    position: absolute;
    left: 96px;
    top: 10px;
    display: flex;
    align-items: center;
    gap: 8px;
    font-size: 11px;
    letter-spacing: 0.08em;
    text-transform: uppercase;
  }
  .brand {
    position: absolute;
    left: 50%;
    top: 4px;
    transform: translateX(-50%);
    font-family: "Anton", sans-serif;
    font-size: 22px;
    letter-spacing: 0.12em;
    text-transform: uppercase;
    white-space: nowrap;
  }
  .cart {
    position: absolute;
    right: 124px;
    top: 8px;
  }
  .smoke {
    position: absolute;
    left: 0;
    bottom: 0;
    width: 420px;
    height: 200px;
    background: radial-gradient(ellipse at 30% 85%, var(--smoke), transparent 65%);
  }
  .duo-photo {
    position: absolute;
    left: 396px;
    top: 272px;
    width: 276px;
    height: 528px;
    background: linear-gradient(180deg, var(--photo-mid) 0%, var(--photo-light) 35%, var(--photo-dark) 75%, var(--ink) 100%);
    border-radius: 60px 60px 0 0;
    opacity: 0.9;
  }
  .headline {
    font-family: "Anton", sans-serif;
    font-weight: 400;
    text-transform: uppercase;
    line-height: 1;
  }
  .headline span {
    position: absolute;
    display: block;
    color: var(--paper);
  }
  .headline .word-tag { left: 252px; top: 318px; font-size: 140px; letter-spacing: -0.02em; }
  .headline .word-team { left: 540px; top: 414px; font-size: 140px; letter-spacing: -0.02em; }
  .headline .word-duo { left: 420px; top: 550px; font-size: 170px; letter-spacing: -0.02em; }
</style>
</head>
<body>
  <main class="hero">
    <div class="smoke" role="img" aria-label="Soft drifting smoke along the floor"></div>
    <div class="duo-photo" role="img" aria-label="Photo of the two hosts standing side by side in dark outfits and sunglasses"></div>

    <header class="site-header">
      <div class="menu-toggle">
        <svg width="12" height="9" viewBox="0 0 12 9" aria-hidden="true">
          <rect x="0" y="0" width="12" height="1.4" fill="#fff"/>
          <rect x="0" y="3.8" width="12" height="1.4" fill="#fff"/>
          <rect x="0" y="7.6" width="8" height="1.4" fill="#fff"/>
        </svg>
        <span>Menu</span>
      </div>
      <div class="brand">Velm Kor Studio</div>
      <div class="cart" aria-label="Cart">
        <svg width="18" height="16" viewBox="0 0 18 16" fill="none" stroke="#fff" stroke-width="1.4" aria-hidden="true">
          <path d="M1 1h3l2 9h9l2-6H5"/>
          <circle cx="7" cy="14" r="1.2"/>
          <circle cx="14" cy="14" r="1.2"/>
        </svg>
      </div>
    </header>

    <h1 class="headline">
      <span class="word-tag">Tag</span>
      <span class="word-team">Team</span>
      <span class="word-duo">Duo</span>
    </h1>
  </main>
</body>
</html>
```